Bref créative
KORVO FREIGHT
BUSINESS CARDS AND BROCHURE LAYOUT
Professional
Reed Quandt
Owner/Specialist
I want no address
korvofreight@nubramail.com
www.korvofreight-example.com
just the logo on the back

```html
<!DOCTYPE html>
<html lang="en">
<head>
<meta charset="utf-8">
<title>Korvo Freight Brochure</title>
<link rel="stylesheet" href="https://fonts.googleapis.com/css2?family=Open+Sans:wght@400;700;800&display=swap">
<style>
  :root{
    --red:#c8202f;
    --red-dark:#9e1522;
    --ink:#3a3a3a;
    --grey:#d7d7d9;
    --grey-dark:#8d8f94;
    --paper:#ffffff;
    --stage:#ecebe8;
  }
  *{box-sizing:border-box;margin:0;padding:0}
  html,body{width:1200px;height:664px;overflow:hidden}
  body{background:var(--stage);font-family:"Open Sans",Arial,sans-serif;position:relative}
  .sheet{position:absolute;top:75px;width:389px;height:514px;background:var(--paper);box-shadow:0 2px 8px rgba(0,0,0,.18);overflow:hidden}
  .sheet--outer{left:202px}
  .sheet--inner{left:608px}
  .panel{position:absolute;top:0;width:194.5px;height:514px;overflow:hidden}
  .panel--left{left:0}
  .panel--right{left:194.5px}
  .panel svg{position:absolute;inset:0;width:100%;height:100%}
  .photo-fill{position:absolute;left:0;top:0;width:100%;height:146px;background:linear-gradient(160deg,#b9cde0 0%,#eef2f6 45%,#6d6f75 100%)}
  .about{position:absolute;left:0;top:146px;width:100%;bottom:0;background:var(--red)}
  .tab{display:inline-block;background:var(--red-dark);color:#fff;font-weight:800;font-size:11px;letter-spacing:.5px;padding:4px 14px 3px}
  .about .tab{margin-top:10px;border-bottom:2px solid #fff;width:120px}
  .copy{font-size:7.6px;line-height:1.45;padding:0 14px}
  .copy p{margin-top:8px}
  .copy--light{color:#fff}
  .copy--dark{color:var(--ink)}
  .brand{position:absolute;display:flex;align-items:center;gap:6px;left:0;width:100%;justify-content:center}
  .brand__mark{width:12px;height:12px;background:var(--red)}
  .brand__name{font-size:17px;font-weight:800;color:var(--red);letter-spacing:.3px}
  .tagline{position:absolute;width:100%;text-align:center;font-size:6.5px;color:var(--grey-dark)}
  .heading-bar{position:absolute;left:0;top:22px;width:160px;background:var(--red);color:#fff;font-weight:800;font-size:10.5px;padding:5px 12px;border-radius:0 12px 12px 0}
  .inner-copy{position:absolute;top:48px;left:0;width:100%}
  .features-label{position:absolute;left:12px;top:78px;background:var(--red-dark);color:#fff;font-weight:800;font-size:10.5px;padding:4px 12px;border:1.5px solid #fff}
  .feature-box{position:absolute;left:10px;right:10px;border:1.5px solid #fff}
  .feature-box--one{top:112px;height:150px}
  .feature-box--two{top:290px;height:150px}
  .feature-photo{position:absolute;right:6px;top:8px;width:72px;height:80px;background:linear-gradient(180deg,#dfe3e8,#9aa0a8)}
  .feature-box .copy{padding:0 8px}
  .feature-box--one .copy{width:100px}
</style>
</head>
<body>

<section class="sheet sheet--outer">
  <div class="panel panel--left">
    <div class="photo-fill" role="img" aria-label="Photo of a delivery truck being loaded with boxes"></div>
    <div class="about">
      <h2 class="tab">ABOUT US</h2>
      <div class="copy copy--light">
        <p>We move freight across the region with care, speed and clear tracking. Every load is planned by our team, checked at each stop and delivered on time to the door.</p>
        <p>We move freight across the region with care, speed and clear tracking. Every load is planned by our team, checked at each stop and delivered on time to the door.</p>
        <p>We move freight across the region with care, speed and clear tracking. Every load is planned by our team, checked at each stop and delivered on time to the door.</p>
      </div>
    </div>
  </div>
  <div class="panel panel--right">
    <svg viewBox="0 0 195 514" preserveAspectRatio="none">
      <path d="M0 48 Q100 12 195 0 L195 26 Q100 34 0 62Z" fill="var(--grey)"/>
      <path d="M40 44 Q120 14 195 8 L195 20 Q120 26 40 44Z" fill="var(--red)"/>
      <path d="M0 250 Q100 218 195 232 L195 250 Q100 238 0 266Z" fill="var(--red)"/>
      <path d="M0 240 Q100 210 195 222 L195 232 Q100 218 0 250Z" fill="var(--grey)"/>
      <path d="M0 266 Q100 238 195 250 L195 470 Q100 492 0 470Z" fill="url(#vanFill)" role="img" aria-label="Photo of a white delivery van outside a warehouse"/>
      <path d="M0 470 Q100 492 195 470 L195 514 L0 514Z" fill="var(--red)"/>
      <defs>
        <linearGradient id="vanFill" x1="0" y1="0" x2="0" y2="1">
          <stop offset="0" stop-color="#c9d6e3"/>
          <stop offset=".55" stop-color="#eef0f2"/>
          <stop offset="1" stop-color="#8f9399"/>
        </linearGradient>
      </defs>
    </svg>
    <div class="brand" style="top:128px"><span class="brand__mark"></span><span class="brand__name">KORVO FREIGHT</span></div>
    <p class="tagline" style="top:152px">Freight handled with care</p>
  </div>
</section>

<section class="sheet sheet--inner">
  <div class="panel panel--left">
    <h2 class="heading-bar">ADVANCEMENT IN BUSSINES</h2>
    <div class="inner-copy copy copy--dark">
      <p>We move freight across the region with care, speed and clear tracking. Every load is planned by our team, checked at each stop and delivered on time to the door.</p>
      <p>We move freight across the region with care, speed and clear tracking. Every load is planned by our team, checked at each stop and delivered on time to the door.</p>
      <p>We move freight across the region with care, speed and clear tracking. Every load is planned by our team, checked at each stop and delivered on time to the door.</p>
    </div>
    <svg viewBox="0 0 195 514" preserveAspectRatio="none">
      <path d="M0 432 Q100 412 195 424 L195 434 Q100 424 0 444Z" fill="var(--grey)"/>
      <path d="M0 444 Q100 424 195 434 L195 442 Q100 434 0 452Z" fill="var(--red)"/>
      <path d="M0 498 Q100 490 195 496 L195 514 L0 514Z" fill="var(--red)"/>
    </svg>
    <div class="brand" style="top:462px"><span class="brand__mark"></span><span class="brand__name">KORVO FREIGHT</span></div>
  </div>
  <div class="panel panel--right">
    <svg viewBox="0 0 195 514" preserveAspectRatio="none">
      <path d="M0 70 Q80 30 195 20 L195 514 L0 514Z" fill="var(--red)"/>
      <path d="M0 60 Q80 22 195 10 L195 20 Q80 30 0 70Z" fill="var(--grey)"/>
      <path d="M0 470 Q100 450 195 462 L195 474 Q100 464 0 482Z" fill="var(--red-dark)"/>
    </svg>
    <h2 class="features-label">FEATURES</h2>
    <div class="feature-box feature-box--one">
      <div class="feature-photo" role="img" aria-label="Photo of a delivery truck on the road"></div>
      <div class="copy copy--light"><p>Fast pickup, live tracking and safe handling for every order we carry.</p></div>
    </div>
    <div class="feature-box feature-box--two">
      <div class="copy copy--light"><p>We move freight across the region with care, speed and clear tracking. Every load is planned by our team, checked at each stop and delivered on time to the door.</p></div>
    </div>
  </div>
</section>

</body>
</html>
```